Priority Goals poster for school year

We are an elementary school and the past two years have had you help us to design a "poster" that illustrates our goal of the coming year. I am attaching our last year's one, along with some photos of our (ver rough) thinking for next years. The priority goal at top remains the same. Can't wait to see your genius ideas! :)

Target Market(s)

Staff of an elementary school and parents to some (informative) extent as well.

Colors
296eb1
6094c6
fbed22
fbee3f

Requirements
Must have
• items from the white board picture we have attached

```html
<!DOCTYPE html>
<html lang="en">
<head>
<meta charset="utf-8">
<title>Cedar Ridge Elementary School – 2020-2021 Priority Goals</title>
<link rel="stylesheet" href="https://fonts.googleapis.com/css2?family=Anton&family=Montserrat:wght@400;500;600;700&display=swap">
<style>
  :root {
    --navy: #2b3a97;
    --navy-deep: #15226a;
    --gold: #f0cb16;
    --gold-text: #e2bc0c;
    --sky: #3277bb;
    --ink: #1e1e1e;
    --paper: #ececec;
    --white: #ffffff;
  }
  * { margin: 0; padding: 0; box-sizing: border-box; }
  html, body { width: 800px; height: 1200px; overflow: hidden; background: var(--paper); }
  body { font-family: "Montserrat", sans-serif; color: var(--ink); }

  .poster { position: relative; width: 800px; height: 1200px; overflow: hidden;
    background: linear-gradient(135deg, #e6e6e6 0%, #f7f7f7 45%, #e9e9e9 70%, #f4f4f4 100%); }

  .header { position: absolute; left: 0; top: 0; width: 800px; height: 182px; background: #f1f1f1; }
  .header svg { position: absolute; left: 0; top: 0; }
  .year { position: absolute; left: 65px; top: 38px; font-size: 40px; font-weight: 400; color: var(--white); letter-spacing: 1px; line-height: 1; }
  .headline { position: absolute; left: 64px; top: 82px; font-family: "Anton", sans-serif; font-weight: 400; font-size: 68px; line-height: 1; color: var(--gold); letter-spacing: 1px; }
  .school-name { position: absolute; left: 590px; top: 58px; width: 180px; text-align: center; font-weight: 700; color: var(--navy); font-size: 22px; line-height: 1.1; }
  .school-name small { display: block; font-size: 13px; letter-spacing: 0.5px; margin-top: 4px; }

  .goals { position: absolute; left: 0; top: 182px; width: 800px; height: 120px; background: #ebebeb; display: flex; padding-top: 30px; }
  .goal { font-size: 15px; font-weight: 600; text-align: center; line-height: 1.4; letter-spacing: 0.3px; height: 56px; }
  .goal + .goal { border-left: 1px dotted #555; }
  .goal:nth-child(1) { width: 250px; padding-left: 14px; }
  .goal:nth-child(2) { width: 179px; }
  .goal:nth-child(3) { width: 211px; }
  .goal:nth-child(4) { width: 160px; }

  .wheel { position: absolute; left: 98px; top: 321px; width: 600px; height: 600px; }
  .segment { position: absolute; text-align: center; font-weight: 700; transform: translateX(-50%); }
  .segment h3 { font-size: 13.5px; font-weight: 700; line-height: 1.15; letter-spacing: 0.3px; }
  .segment p { font-size: 10.5px; font-weight: 700; line-height: 1.3; margin-top: 4px; }
  .segment .icon { width: 28px; height: 28px; margin: 0 auto 6px; border-radius: 6px; }
  .seg-top, .seg-bottom { color: var(--navy-deep); }
  .seg-top .icon, .seg-bottom .icon { background: rgba(21,34,106,0.25); }
  .seg-left, .seg-right { color: var(--white); }
  .seg-left .icon, .seg-right .icon { background: rgba(255,255,255,0.35); }
  .seg-top { left: 402px; top: 365px; width: 170px; }
  .seg-left { left: 200px; top: 566px; width: 110px; }
  .seg-right { left: 597px; top: 571px; width: 140px; }
  .seg-right p { margin-top: 16px; }
  .seg-bottom { left: 404px; top: 781px; width: 200px; }

  .promise { position: absolute; left: 0; top: 944px; width: 800px; text-align: center; font-family: "Anton", sans-serif; font-weight: 400; font-size: 72px; line-height: 1; letter-spacing: -0.5px; }
  .promise .blue { color: var(--navy); }
  .promise .gold { color: var(--gold-text); }
  .tagline { position: absolute; left: 0; top: 1024px; width: 800px; text-align: center; font-size: 31px; font-weight: 400; letter-spacing: 0.5px; }

  .footer { position: absolute; left: 0; top: 1093px; width: 800px; height: 107px; }
  .footer svg.band { position: absolute; left: 0; top: 0; }
  .contact { position: absolute; display: flex; align-items: center; gap: 12px; font-weight: 700; }
  .contact.phone { left: 52px; top: 21px; font-size: 24px; color: var(--ink); letter-spacing: 1px; }
  .contact.social { left: 52px; top: 55px; font-size: 17px; color: var(--ink); letter-spacing: 1px; }
  .contact.web { left: 398px; top: 25px; font-size: 14px; color: var(--white); letter-spacing: 0.5px; }
  .contact.address { left: 398px; top: 55px; font-size: 14px; color: var(--white); letter-spacing: 0.5px; }
  .social-mark { width: 13px; height: 13px; border: 2px solid var(--navy); border-radius: 3px; }
</style>
</head>
<body>
<main class="poster">

  <header class="header">
    <svg width="800" height="182" viewBox="0 0 800 182" aria-hidden="true">
      <path d="M0 0 H800 V10 H640 C590 10 575 70 560 115 C545 158 510 176 470 176 H0 Z" fill="#ffffff"/>
      <path d="M0 0 H800 V10 H628 C585 10 568 70 552 115 C538 156 505 172 465 172 H0 Z" fill="var(--gold)"/>
      <path d="M0 0 H800 V10 H590 C565 12 552 60 538 105 C524 150 500 167 455 167 H0 Z" fill="#ffffff"/>
      <path d="M0 0 H800 V10 H582 C558 14 546 62 532 105 C518 148 495 165 450 165 H0 Z" fill="var(--navy)"/>
      <rect x="0" y="169" width="800" height="7" fill="#ffffff"/>
    </svg>
    <div class="year">2020-2021</div>
    <h1 class="headline">PRIORITY GOALS</h1>
    <div class="school-name">CEDAR RIDGE<small>ELEMENTARY SCHOOL</small></div>
  </header>

  <section class="goals">
    <div class="goal">Be intentional with<br>padr actor-focus</div>
    <div class="goal">Staff douing what<br>they love teaching</div>
    <div class="goal">Mental health wellness<br>for every person in out<br>school community</div>
    <div class="goal">Broken<br>ovr leas</div>
  </section>

  <svg class="wheel" viewBox="-300 -300 600 600" aria-hidden="true">
    <defs>
      <filter id="soft-shadow" x="-20%" y="-20%" width="140%" height="140%">
        <feDropShadow dx="0" dy="4" stdDeviation="6" flood-color="#000" flood-opacity="0.25"/>
      </filter>
    </defs>
    <circle r="268" fill="var(--navy-deep)"/>
    <g filter="url(#soft-shadow)">
      <path d="M -171.7 -223.7 A 282 282 0 0 1 171.7 -223.7 L 85.2 -111.1 A 140 140 0 0 0 -85.2 -111.1 Z" fill="var(--gold)"/>
      <path d="M -171.7 -223.7 A 282 282 0 0 1 171.7 -223.7 L 85.2 -111.1 A 140 140 0 0 0 -85.2 -111.1 Z" fill="var(--sky)" transform="rotate(90)"/>
      <path d="M -171.7 -223.7 A 282 282 0 0 1 171.7 -223.7 L 85.2 -111.1 A 140 140 0 0 0 -85.2 -111.1 Z" fill="var(--gold)" transform="rotate(180)"/>
      <path d="M -171.7 -223.7 A 282 282 0 0 1 171.7 -223.7 L 85.2 -111.1 A 140 140 0 0 0 -85.2 -111.1 Z" fill="var(--sky)" transform="rotate(270)"/>
    </g>
    <circle r="124" fill="#ffffff" filter="url(#soft-shadow)"/>
    <circle r="108" fill="var(--navy)" role="img" aria-label="School mascot illustration: a walking bear in gold and navy"/>
  </svg>

  <div class="segment seg-top">
    <div class="icon" role="img" aria-label="Speaking head icon"></div>
    <h3>VOICE OF ALL</h3>
    <p>Who are we?<br>Where are we going?</p>
  </div>
  <div class="segment seg-left">
    <div class="icon" role="img" aria-label="Ruler and measuring icon"></div>
    <h3>SMALL<br>MEASURED</h3>
    <p>Step towards<br>higer goal</p>
  </div>
  <div class="segment seg-right">
    <div class="icon" role="img" aria-label="Communication icon"></div>
    <h3>COMMUNICATE</h3>
    <p>Eypectahare<br>Support<br>Far clarity</p>
  </div>
  <div class="segment seg-bottom">
    <div class="icon" role="img" aria-label="Handshake icon"></div>
    <h3>BUILD VALUE<br>PARTNERSHIPS</h3>
    <p>Connect, Celebrate Strong,<br>Predictions Laugh, have fun</p>
  </div>

  <h2 class="promise"><span class="blue">FOUNDATIONAL</span> <span class="gold">PROMISES</span></h2>
  <p class="tagline">(4 Years strong, better everydat)</p>

  <footer class="footer">
    <svg class="band" width="800" height="107" viewBox="0 0 800 107" aria-hidden="true">
      <rect width="800" height="107" fill="var(--navy)"/>
      <path d="M0 0 H372 C352 8 345 40 330 65 C315 92 295 105 260 107 H0 Z" fill="#ffffff"/>
      <path d="M0 0 H362 C342 8 336 40 322 64 C308 90 288 103 255 107 H0 Z" fill="var(--gold)"/>
    </svg>
    <div class="contact phone">
      <svg width="18" height="18" viewBox="0 0 24 24" aria-hidden="true"><path d="M6.6 10.8a15.2 15.2 0 0 0 6.6 6.6l2.2-2.2a1 1 0 0 1 1-.25 11.4 11.4 0 0 0 3.6.57 1 1 0 0 1 1 1V20a1 1 0 0 1-1 1A17 17 0 0 1 3 4a1 1 0 0 1 1-1h3.5a1 1 0 0 1 1 1c0 1.25.2 2.45.57 3.6a1 1 0 0 1-.25 1z" fill="var(--navy)"/></svg>
      <span>555-014-3600</span>
    </div>
    <div class="contact social">
      <span class="social-mark"></span>
      <span>@cedarridgelearners</span>
    </div>
    <div class="contact web">
      <svg width="14" height="14" viewBox="0 0 24 24" aria-hidden="true"><g fill="none" stroke="var(--gold)" stroke-width="2"><circle cx="12" cy="12" r="10"/><ellipse cx="12" cy="12" rx="4" ry="10"/><path d="M2 12h20M4 7h16M4 17h16"/></g></svg>
      <span>cedarridge.example.edu</span>
    </div>
    <div class="contact address">
      <svg width="14" height="16" viewBox="0 0 24 28" aria-hidden="true"><path d="M12 0a10 10 0 0 0-10 10c0 7.5 10 18 10 18s10-10.5 10-18A10 10 0 0 0 12 0zm0 14a4 4 0 1 1 0-8 4 4 0 0 1 0 8z" fill="var(--gold)"/></svg>
      <span>1200 Birch Hollow Rd., Fernwood, WA 98000</span>
    </div>
  </footer>

</main>
</body>
</html>
```